Business Card Design Project

Business card design based on the existing logo.

Target Market(s)

Small to medium business owners and CIO's looking for professional IT services.

Industry/Entity Type

Business

Font styles to use
Serif
Sans Serif

Requirements
Must have
• Logo, company name, company details

Text to appear on the business card
Name / Title:
Leon Fairholt
CEO

Address:
Valtiro Limited
Level 3, 42 Kestle St
P O Box 462
Paraparaumu 5391

Other details:
leon@valtiro.co
Ph: 0800 519 308
Mob: +64 21 948 216
www.valtiro.co

Nice to have
• I would look at both single and double sided options. My initial thought is double sided with just the logo with the grey framing for the front and the name and details on the back. But I'm open to other design options.

```html
<!DOCTYPE html>
<html lang="en">
<head>
<meta charset="utf-8">
<title>Valtiro Business Card</title>
<link href="https://fonts.googleapis.com/css2?family=Open+Sans:wght@400;600;700&family=Cormorant+SC:wght@600&display=swap" rel="stylesheet">
<style>
  :root {
    --brand-blue: #1e6583;
    --ink: #111111;
    --paper: #ffffff;
    --backdrop: #8d8d8d;
  }
  * { box-sizing: border-box; margin: 0; padding: 0; }
  html, body {
    width: 1200px; height: 900px; overflow: hidden;
    background: var(--backdrop);
  }
  .card {
    position: absolute; left: 150px; top: 200px;
    width: 900px; height: 500px;
    background: var(--brand-blue);
    box-shadow: 0 10px 30px rgba(0,0,0,0.25);
  }
  .card__panel {
    position: absolute; left: 0; right: 0; top: 28px; height: 392px;
    background: var(--paper);
    border-radius: 48px 0 48px 48px;
  }
  .brand {
    position: absolute; left: 0; right: 0; top: 70px;
    display: flex; justify-content: center; align-items: center; gap: 26px;
  }
  .brand__dot {
    width: 70px; height: 70px; border-radius: 50%;
    background: var(--brand-blue);
  }
  .brand__name {
    font-family: "Open Sans", sans-serif; font-weight: 400;
    font-size: 96px; line-height: 1; color: var(--ink); letter-spacing: 1px;
  }
  .person {
    position: absolute; left: 40px; top: 318px;
  }
  .person__name {
    font-family: "Cormorant SC", serif; font-weight: 600;
    font-size: 42px; color: var(--brand-blue); line-height: 1;
  }
  .person__title {
    font-family: "Open Sans", sans-serif; font-size: 17px;
    color: var(--brand-blue); margin-top: 8px;
  }
  .divider {
    position: absolute; width: 2px; background: var(--brand-blue);
  }
  .divider--contact { left: 345px; top: 250px; height: 130px; }
  .divider--address { left: 650px; top: 250px; height: 130px; }
  .contact {
    position: absolute; left: 368px; top: 252px;
    display: grid; grid-template-columns: auto auto; column-gap: 18px; row-gap: 6px;
    font-family: "Open Sans", sans-serif; font-size: 17px; line-height: 24px;
  }
  .contact__label { font-weight: 700; color: var(--brand-blue); }
  .contact__value { color: var(--ink); }
  .address {
    position: absolute; left: 672px; top: 252px;
    font-family: "Open Sans", sans-serif; font-size: 17px; line-height: 30px;
    color: var(--ink);
  }
  .address__company { font-weight: 700; color: var(--brand-blue); }
</style>
</head>
<body>
  <div class="card">
    <div class="card__panel"></div>

    <div class="brand">
      <span class="brand__dot"></span>
      <span class="brand__name">Valtiro</span>
    </div>

    <div class="person">
      <div class="person__name">Leon Fairholt</div>
      <div class="person__title">CEO</div>
    </div>

    <div class="divider divider--contact"></div>
    <div class="contact">
      <span class="contact__label">Phone:</span><span class="contact__value">0800 519 308</span>
      <span class="contact__label">Mobile:</span><span class="contact__value">+64 21 948 216</span>
      <span class="contact__label">E-mail:</span><span class="contact__value">leon@valtiro.co</span>
      <span class="contact__label">Website:</span><span class="contact__value">www.valtiro.co</span>
    </div>

    <div class="divider divider--address"></div>
    <div class="address">
      <div class="address__company">Valtiro Limited</div>
      <div>Level 3, 42 Kestle St</div>
      <div>P O Box 462</div>
      <div>Paraparaumu 5391</div>
    </div>
  </div>
</body>
</html>
```